Construction Company Business Card

Business Card Design using new Logo

Contact Information for Business Card

include all company info and website

Requirements
Must have
• Wesley Corman - President
ph. 254-617-0382
Cedar Knoll, TX
wesley@ironmarkframing.com
www.ironmarkframing.com

```html
<!DOCTYPE html>
<html lang="en">
<head>
<meta charset="utf-8">
<title>Ironmark Framing – Business Card</title>
<link href="https://fonts.googleapis.com/css2?family=Raleway:wght@700&family=Josefin+Sans:wght@400&family=Arimo:wght@400;700&display=swap" rel="stylesheet">
<style>
  :root {
    --brand-red: #c8222a;
    --paper: #ffffff;
    --ink-grey: #5a5a5a;
    --rule-grey: #a8a8a8;
    --backdrop: #8c8c8c;
  }
  * { margin: 0; padding: 0; box-sizing: border-box; }
  html, body { width: 1200px; height: 1200px; overflow: hidden; }
  body { background: var(--backdrop); position: relative; }

  .card {
    position: absolute;
    top: 303px;
    width: 368px;
    height: 594px;
  }
  .card--front { left: 201px; background: var(--brand-red); }
  .card--back { left: 600px; background: var(--paper); }

  .brand-name {
    position: absolute;
    left: 0; right: 0;
    text-align: center;
    font-family: "Josefin Sans", sans-serif;
    font-weight: 400;
    font-size: 25px;
    letter-spacing: 1.5px;
    text-transform: uppercase;
  }
  .card--front .brand-name { top: 274px; color: var(--paper); }
  .card--back .brand-name { top: 166px; color: var(--brand-red); }

  .front-url {
    position: absolute;
    left: 0; right: 0;
    top: 541px;
    text-align: center;
    font-family: "Arimo", sans-serif;
    font-weight: 700;
    font-size: 16px;
    letter-spacing: 2.6px;
    color: var(--paper);
  }

  .person-name {
    position: absolute;
    left: 0; right: 0; top: 333px;
    text-align: center;
    font-family: "Raleway", sans-serif;
    font-weight: 700;
    font-size: 21px;
    color: var(--brand-red);
  }
  .person-title {
    position: absolute;
    left: 0; right: 0; top: 361px;
    text-align: center;
    font-family: "Arimo", sans-serif;
    font-size: 16px;
    color: var(--ink-grey);
  }

  .icon-row {
    position: absolute;
    left: 87px; top: 395px;
    width: 190px; height: 26px;
    display: flex; align-items: center; gap: 4px;
  }
  .icon-row .rule { flex: 1; height: 1px; background: var(--rule-grey); margin: 0 4px; }
  .icon-tile {
    width: 25px; height: 25px;
    background: var(--brand-red);
    border-radius: 3px;
    display: flex; align-items: center; justify-content: center;
  }

  .contact-list {
    position: absolute;
    left: 0; right: 0; top: 431px;
    text-align: center;
    font-family: "Arimo", sans-serif;
    font-size: 16px;
    line-height: 21.7px;
    color: var(--ink-grey);
    list-style: none;
  }

  .location-row {
    position: absolute;
    left: 88px; top: 500px;
    width: 195px; height: 26px;
    display: flex; align-items: center; gap: 4px;
  }
  .location-row .rule { flex: 1; height: 1px; background: var(--rule-grey); margin: 0 4px; }
  .location-text {
    position: absolute;
    left: 0; right: 0; top: 531px;
    text-align: center;
    font-family: "Arimo", sans-serif;
    font-size: 17px;
    color: var(--ink-grey);
  }
</style>
</head>
<body>

<section class="card card--front" aria-label="Card front">
  <div class="brand-name">Ironmark Framing</div>
  <div class="front-url">www.ironmarkframing.com</div>
</section>

<section class="card card--back" aria-label="Card back">
  <div class="brand-name">Ironmark Framing</div>

  <h1 class="person-name">WESLEY CORMAN</h1>
  <p class="person-title">President</p>

  <div class="icon-row">
    <span class="rule"></span>
    <span class="icon-tile" aria-label="Phone">
      <svg width="16" height="14" viewBox="0 0 16 14" fill="#fff">
        <path d="M1 4 C1 1 15 1 15 4 L15 5 L11 5 L11 3.5 L5 3.5 L5 5 L1 5 Z"/>
        <path d="M4 6 L12 6 L14 13 L2 13 Z"/>
      </svg>
    </span>
    <span class="icon-tile" aria-label="Email">
      <svg width="16" height="12" viewBox="0 0 16 12" fill="none" stroke="#fff" stroke-width="1.2">
        <rect x="0.6" y="0.6" width="14.8" height="10.8"/>
        <path d="M0.6 0.6 L8 7 L15.4 0.6 M0.6 11.4 L6 5.5 M15.4 11.4 L10 5.5"/>
      </svg>
    </span>
    <span class="icon-tile" aria-label="Website">
      <svg width="16" height="16" viewBox="0 0 16 16" fill="none" stroke="#fff" stroke-width="1.4">
        <circle cx="8" cy="8" r="6.5"/>
        <path d="M1.5 8 H14.5 M8 1.5 C5 5 5 11 8 14.5 C11 11 11 5 8 1.5"/>
      </svg>
    </span>
    <span class="rule"></span>
  </div>

  <ul class="contact-list">
    <li>254-617-0382</li>
    <li>wesley@ironmarkframing.com</li>
    <li>www.ironmarkframing.com</li>
  </ul>

  <div class="location-row">
    <span class="rule"></span>
    <span class="icon-tile" aria-label="Location">
      <svg width="12" height="17" viewBox="0 0 12 17" fill="#fff">
        <path d="M6 0.5 C2.8 0.5 0.5 2.9 0.5 6 C0.5 10 6 16.5 6 16.5 C6 16.5 11.5 10 11.5 6 C11.5 2.9 9.2 0.5 6 0.5 Z M6 3.8 A2.2 2.2 0 1 1 6 8.2 A2.2 2.2 0 1 1 6 3.8 Z"/>
      </svg>
    </span>
    <span class="rule"></span>
  </div>
  <p class="location-text">Cedar Knoll, TX</p>
</section>

</body>
</html>
```